Biz Card for Harrowfield Property Partners - HWPP

Harrowfield Property Partners is a commercial real estate acquisitions firm. We buy commercial property and need to raise capital from investors for each deal we buy. The vibe needs to be: give us your money, we will multiply it.
Our website: www.hrwpp-example.com
Competitors are: https://velmarholdings-example.com/, https://tribanquepartners-example.com/, http://www.ostrellecapital-example.com/
Target Market(s)
High Net Worth Individuals, Bankers, Insurance Companies, Commercial Real Estate Brokers.
Industry/Entity Type
Investment Banking
Contact Information for Business Card
Name, Title, Addess, Cell#, Office#, email, website
Requirements
Must have
- use one of our logos. See website for look and feel: www.hrwpp-example.com
Nice to have
- see website: www.hrwpp-example.com

```html
<!DOCTYPE html>
<html lang="en">
<head>
<meta charset="utf-8">
<title>Harrowfield Property Partners – Business Card</title>
<link rel="stylesheet" href="https://fonts.googleapis.com/css2?family=Lato:wght@400;700&family=Montserrat:wght@400;500;600&display=swap">
<style>
  :root {
    --ink: #0d0d0d;
    --paper: #ffffff;
    --backdrop: #ecebe8;
    --soft-grey: #ececec;
    --rule-grey: #9a9a9a;
    --muted: #555555;
  }
  * { box-sizing: border-box; margin: 0; padding: 0; }
  html, body { width: 1200px; height: 750px; overflow: hidden; }
  body {
    background: var(--backdrop);
    font-family: "Montserrat", sans-serif;
    color: var(--ink);
    position: relative;
  }
  .card {
    position: absolute;
    width: 540px;
    height: 309px;
    background: var(--paper);
    overflow: hidden;
    box-shadow: 0 12px 30px rgba(0,0,0,0.12);
  }
  .card--front { left: 30px; top: 220px; border-top: 8px solid var(--ink); border-bottom: 8px solid var(--ink); }
  .card--back { left: 630px; top: 220px; border-top: 5px solid var(--ink); border-bottom: 7px solid var(--ink); }

  /* front */
  .front-mark {
    position: absolute;
    left: 0; right: 0; top: 92px;
    display: flex; align-items: center; justify-content: center; gap: 16px;
  }
  .mark-circle { border-radius: 50%; background: var(--ink); flex: none; }
  .front-mark .mark-circle { width: 62px; height: 62px; }
  .wordmark { font-family: "Lato", sans-serif; font-weight: 400; color: var(--ink); }
  .front-mark .wordmark__name { font-size: 27px; letter-spacing: 5px; line-height: 1; display: block; }
  .front-mark .wordmark__sub { font-size: 9px; letter-spacing: 5px; display: block; margin-top: 8px; }

  /* back */
  .back-mark { position: absolute; left: 24px; top: 20px; display: flex; align-items: center; gap: 10px; }
  .back-mark .mark-circle { width: 44px; height: 44px; }
  .back-mark .wordmark__name { font-size: 17px; letter-spacing: 3px; display: block; line-height: 1; }
  .back-mark .wordmark__sub { font-size: 6.5px; letter-spacing: 3.2px; display: block; margin-top: 5px; }
  .back-rule { position: absolute; left: 76px; top: 76px; width: 270px; height: 1px; background: var(--rule-grey); }

  .person { position: absolute; right: 24px; top: 24px; text-align: right; }
  .person__name { font-size: 13px; font-weight: 600; letter-spacing: 0.5px; display: block; }
  .person__title { font-size: 8px; letter-spacing: 1.5px; color: var(--muted); display: block; margin-top: 4px; text-transform: uppercase; }

  .contact-list { position: absolute; left: 26px; top: 86px; list-style: none; font-size: 9px; line-height: 1.3; }
  .contact-list li { display: flex; align-items: flex-start; gap: 9px; margin-bottom: 4px; }
  .contact-list svg { width: 10px; height: 10px; flex: none; margin-top: 1px; }
  .contact-label { display: inline-block; width: 36px; color: var(--muted); }

  .office {
    position: absolute;
    border: 1px solid var(--rule-grey);
    border-radius: 6px;
    padding: 6px 9px;
    font-size: 7px;
    line-height: 1.3;
    background: rgba(255,255,255,0.85);
  }
  .office svg { width: 7px; height: 7px; vertical-align: -1px; margin-right: 2px; }
  .office--gt { left: 18px; top: 212px; width: 178px; }
  .office--ve { left: 214px; top: 230px; width: 150px; }

  .back-decor {
    position: absolute;
    left: 370px; top: 150px;
    width: 300px; height: 300px;
    border-radius: 50%;
    background: var(--soft-grey);
  }
</style>
</head>
<body>

<section class="card card--front" aria-label="Business card front">
  <div class="front-mark">
    <span class="mark-circle"></span>
    <span class="wordmark">
      <span class="wordmark__name">HARROWFIELD</span>
      <span class="wordmark__sub">PROPERTY PARTNERS</span>
    </span>
  </div>
</section>

<section class="card card--back" aria-label="Business card back">
  <div class="back-decor"></div>

  <div class="back-mark">
    <span class="mark-circle"></span>
    <span class="wordmark">
      <span class="wordmark__name">HARROWFIELD</span>
      <span class="wordmark__sub">PROPERTY PARTNERS</span>
    </span>
  </div>
  <div class="back-rule"></div>

  <div class="person">
    <span class="person__name">Marcus Ellery</span>
    <span class="person__title">Managing Partner</span>
  </div>

  <ul class="contact-list">
    <li>
      <svg viewBox="0 0 24 24" aria-hidden="true"><path fill="currentColor" d="M6.6 10.8a15 15 0 0 0 6.6 6.6l2.2-2.2a1 1 0 0 1 1-.25 11.4 11.4 0 0 0 3.6.57 1 1 0 0 1 1 1V20a1 1 0 0 1-1 1A17 17 0 0 1 3 4a1 1 0 0 1 1-1h3.5a1 1 0 0 1 1 1c0 1.25.2 2.45.57 3.6a1 1 0 0 1-.25 1z"/></svg>
      <span><span class="contact-label">Cell</span>(305) 555-0162</span>
    </li>
    <li>
      <svg viewBox="0 0 24 24" aria-hidden="true"><path fill="currentColor" d="M6.6 10.8a15 15 0 0 0 6.6 6.6l2.2-2.2a1 1 0 0 1 1-.25 11.4 11.4 0 0 0 3.6.57 1 1 0 0 1 1 1V20a1 1 0 0 1-1 1A17 17 0 0 1 3 4a1 1 0 0 1 1-1h3.5a1 1 0 0 1 1 1c0 1.25.2 2.45.57 3.6a1 1 0 0 1-.25 1z"/></svg>
      <span><span class="contact-label">Office</span>(305) 555-0148</span>
    </li>
    <li>
      <svg viewBox="0 0 24 24" aria-hidden="true" fill="none" stroke="currentColor" stroke-width="2"><rect x="2" y="5" width="20" height="14" rx="2"/><path d="M2 6l10 7 10-7"/></svg>
      <span>m.ellery@hrwpp-example.com</span>
    </li>
    <li>
      <svg viewBox="0 0 24 24" aria-hidden="true" fill="none" stroke="currentColor" stroke-width="1.8"><circle cx="12" cy="12" r="10"/><path d="M2 12h20M12 2c3 3 3 17 0 20M12 2c-3 3-3 17 0 20"/></svg>
      <span>www.hrwpp-example.com</span>
    </li>
    <li>
      <svg viewBox="0 0 24 24" aria-hidden="true"><path fill="currentColor" d="M12 2a7 7 0 0 0-7 7c0 5 7 13 7 13s7-8 7-13a7 7 0 0 0-7-7zm0 9.5A2.5 2.5 0 1 1 12 6.5a2.5 2.5 0 0 1 0 5z"/></svg>
      <span>USA: 480 Larkmoor Ave, Suite 910<br>Westbrook, FL 33190</span>
    </li>
  </ul>

  <div class="office office--gt">
    Guatemala:<br>
    7a. Calle 22-40 Zona 4 Torre<br>
    Norte en Plaza Alcaván,<br>
    Nivel 6, Oficina 604.<br>
    Guatemala, C.A.<br>
    <svg viewBox="0 0 24 24" aria-hidden="true"><path fill="currentColor" d="M6.6 10.8a15 15 0 0 0 6.6 6.6l2.2-2.2a1 1 0 0 1 1-.25 11.4 11.4 0 0 0 3.6.57 1 1 0 0 1 1 1V20a1 1 0 0 1-1 1A17 17 0 0 1 3 4a1 1 0 0 1 1-1h3.5a1 1 0 0 1 1 1c0 1.25.2 2.45.57 3.6a1 1 0 0 1-.25 1z"/></svg>(502) 2555-0193
  </div>

  <div class="office office--ve">
    Venezuela:<br>
    Av Los Almendros,<br>
    Edif Centro Valtera, Ofc PB-C,<br>
    Caracas 1090.<br>
    <svg viewBox="0 0 24 24" aria-hidden="true"><path fill="currentColor" d="M6.6 10.8a15 15 0 0 0 6.6 6.6l2.2-2.2a1 1 0 0 1 1-.25 11.4 11.4 0 0 0 3.6.57 1 1 0 0 1 1 1V20a1 1 0 0 1-1 1A17 17 0 0 1 3 4a1 1 0 0 1 1-1h3.5a1 1 0 0 1 1 1c0 1.25.2 2.45.57 3.6a1 1 0 0 1-.25 1z"/></svg>(58) 212 555.01.72
  </div>
</section>

</body>
</html>
```